Havenry - "Where Pest Control is Free for Life..." Please see pitch deck...

Project goal, that this is a reusable template, not a one-off card
Brand and design direction, follow the logo, use the brand palette (with a color swatch table), typography and layout guidance
The Mark Vale placeholder content as a clean field-by-field table (name, title, company, address, office, cell, fax, email, havenry.com)
Print specs, 3.5 × 2 in trim, 0.125 in bleed, 300 DPI, CMYK, crop marks
Deliverables, layered editable PSD (your primary ask) plus vector .AI/.EPS and a press-ready PDF/X-1a, with fonts packaged
What you'll provide (logo, colors, fonts)
Process and sign-off, concept first, then full file package on approval.
Populate every field with this Mark Vale placeholder data so we can see the layout fully built out. We will replace it per person.
Name Mark Vale
Title Title / Position
Company Havenry
Address 487 Orchard Lane, Suite 210, Tallahassee, FL 32308
Office (850) 555-0142
Cell (850) 555-0167
Fax (850) 555-0181
Email markvale@havenry.com
Website havenry.com

We need the working, editable source files so we can update them ourselves, plus a ready-to-print export:
1. Photoshop (.PSD) — fully layered and editable, with each contact field on its own labeled text layer. This is the primary requested format.
2. Vector source — the press-standard editable format, Adobe Illustrator (.AI) and/or .EPS, since vector is preferred for crisp text and logos at print.
3. Print-ready PDF — press-quality (PDF/X-1a), CMYK, with bleed and crop marks, both sides.
4. Packaged fonts and links — include or list all fonts used, and package any linked assets so the files open correctly on our end.

Why both PSD and vector
The PSD covers our request directly and is easy for us to edit. Vector (.AI/.EPS) is what most commercial printers actually prefer for type and logos because it stays razor-sharp at any size. Providing both keeps us flexible no matter which printer we use. Have fun and keep it modern and cool the designer of the logo did a great job, see what you can do.

```html
<!DOCTYPE html>
<html lang="en">
<head>
<meta charset="utf-8">
<title>Havenry Business Card – Concept 03</title>
<link rel="stylesheet" href="https://fonts.googleapis.com/css2?family=Montserrat:wght@400;500;600;700;800&display=swap">
<style>
  :root {
    --backdrop: #ece6e1;
    --navy: #141b33;
    --teal: #17a9b8;
    --teal-bright: #1fb8c6;
    --paper: #f1f1ef;
    --ink: #1d1f26;
    --muted: #565656;
    --white: #ffffff;
  }
  * { box-sizing: border-box; margin: 0; padding: 0; }
  html, body { width: 1200px; height: 1067px; overflow: hidden; }
  body {
    position: relative;
    background: var(--backdrop);
    font-family: "Montserrat", sans-serif;
    color: var(--ink);
  }

  .board-heading {
    position: absolute; left: 0; right: 0; top: 46px;
    text-align: center;
    font-size: 40px; font-weight: 700; letter-spacing: 11px;
    color: var(--teal);
  }
  .board-intro {
    position: absolute; left: 0; right: 0; top: 102px;
    text-align: center;
    font-size: 19px; font-weight: 500; letter-spacing: 1.2px; line-height: 36px;
    color: var(--muted);
  }

  .card {
    position: absolute; top: 208px;
    width: 362px; height: 613px;
    overflow: hidden;
  }
  .card--front { left: 197px; background: var(--paper); }
  .card--back  { left: 661px; background: var(--navy); }

  .card__dark { position: absolute; left: 0; right: 0; background: var(--navy); }
  .card__light { position: absolute; left: 0; right: 0; background: var(--paper); }
  .card__band {
    position: absolute; left: 0; right: 0; height: 42px;
    background: linear-gradient(90deg, var(--teal), var(--teal-bright), var(--teal));
  }

  .card--front .card__dark { top: 0; height: 317px; }
  .card--front .card__band { top: 317px; }

  .card--back .card__light { top: 0; height: 109px; }
  .card--back .card__band { top: 109px; }

  .brand-name {
    position: absolute; left: 0; right: 0; top: 128px;
    text-align: center;
    font-size: 48px; font-weight: 800; letter-spacing: -1px;
    color: var(--white);
  }

  .holder {
    position: absolute; left: 0; right: 0; top: 460px;
    text-align: center;
  }
  .holder__name {
    font-size: 42px; font-weight: 800; letter-spacing: -0.5px;
    color: var(--teal);
    line-height: 1.1;
  }
  .holder__title {
    margin-top: 10px;
    font-size: 15px; font-weight: 500; letter-spacing: 3.2px;
    color: var(--ink);
  }

  .contact-list {
    position: absolute; left: 52px; top: 233px;
    list-style: none;
  }
  .contact-list__item {
    display: flex; align-items: center;
    height: 19px; margin-bottom: 8px;
    font-size: 13.5px; font-weight: 500; letter-spacing: 1.6px;
    color: var(--white);
  }
  .contact-list__item:nth-child(n+3) { margin-bottom: 7.5px; }
  .contact-list__icon {
    width: 19px; height: 19px; margin-right: 19px; flex: none;
  }

  .address {
    position: absolute; left: 54px; top: 479px;
    font-size: 13.5px; font-weight: 500; letter-spacing: 1.8px; line-height: 17px;
    color: var(--teal-bright);
  }

  .brand-vertical {
    position: absolute; left: 296px; top: 522px;
    transform: rotate(-90deg); transform-origin: left top;
    font-size: 27px; font-weight: 800; letter-spacing: -0.5px;
    color: var(--white);
    white-space: nowrap;
  }

  .deliverables {
    position: absolute; left: 0; right: 0; top: 873px;
    text-align: center;
    color: var(--teal);
    font-size: 19.5px; font-weight: 500;
  }
  .deliverables__heading { margin-bottom: 26px; }
  .deliverables__list { list-style: none; line-height: 26px; }
</style>
</head>
<body>

  <h1 class="board-heading">CONCEPT 03</h1>
  <p class="board-intro">A bold, structured business card concept<br>built on contrast, orientation, and modular identity.</p>

  <section class="card card--front" aria-label="Card front">
    <div class="card__dark"></div>
    <p class="brand-name">Havenry</p>
    <div class="card__band" role="img" aria-label="Teal band of window-grid squares"></div>
    <div class="holder">
      <p class="holder__name">Mark Vale</p>
      <p class="holder__title">Title/Position</p>
    </div>
  </section>

  <section class="card card--back" aria-label="Card back">
    <div class="card__light"></div>
    <div class="card__band" role="img" aria-label="Teal band of window-grid squares"></div>

    <ul class="contact-list">
      <li class="contact-list__item">
        <svg class="contact-list__icon" viewBox="0 0 19 19" aria-hidden="true">
          <rect width="19" height="19" rx="3" fill="#17a9b8"/>
          <rect x="4" y="5.5" width="11" height="8" fill="none" stroke="#141b33" stroke-width="1.2"/>
          <path d="M4 5.5l5.5 4.5 5.5-4.5" fill="none" stroke="#141b33" stroke-width="1.2"/>
        </svg>markvale@havenry.com
      </li>
      <li class="contact-list__item">
        <svg class="contact-list__icon" viewBox="0 0 19 19" aria-hidden="true">
          <rect width="19" height="19" rx="3" fill="#17a9b8"/>
          <circle cx="9.5" cy="9.5" r="5.2" fill="none" stroke="#141b33" stroke-width="1.2"/>
          <ellipse cx="9.5" cy="9.5" rx="2.3" ry="5.2" fill="none" stroke="#141b33" stroke-width="1"/>
          <path d="M4.3 9.5h10.4" stroke="#141b33" stroke-width="1"/>
        </svg>havenry.com
      </li>
      <li class="contact-list__item">
        <svg class="contact-list__icon" viewBox="0 0 19 19" aria-hidden="true">
          <rect width="19" height="19" rx="3" fill="#17a9b8"/>
          <rect x="5" y="4" width="9" height="11" fill="none" stroke="#141b33" stroke-width="1.2"/>
          <path d="M7.3 6.5v1.5M9.5 6.5v1.5M11.7 6.5v1.5M7.3 10v1.5M11.7 10v1.5M9.5 12v3" stroke="#141b33" stroke-width="1.1"/>
        </svg>O:&nbsp;&nbsp;(850) 555-0142
      </li>
      <li class="contact-list__item">
        <svg class="contact-list__icon" viewBox="0 0 19 19" aria-hidden="true">
          <rect width="19" height="19" rx="3" fill="#17a9b8"/>
          <path d="M5.5 4.5l2.3-.3 1.1 2.6-1.3 1.1a7 7 0 0 0 3.5 3.5l1.1-1.3 2.6 1.1-.3 2.3c-5 .3-9.3-4-9-9z" fill="none" stroke="#141b33" stroke-width="1.1" stroke-linejoin="round"/>
        </svg>P:&nbsp;&nbsp;(850) 555-0167
      </li>
      <li class="contact-list__item">
        <svg class="contact-list__icon" viewBox="0 0 19 19" aria-hidden="true">
          <rect width="19" height="19" rx="3" fill="#17a9b8"/>
          <rect x="6" y="4" width="7" height="4" fill="none" stroke="#141b33" stroke-width="1.1"/>
          <rect x="4" y="8" width="11" height="5.5" rx="1" fill="none" stroke="#141b33" stroke-width="1.1"/>
          <rect x="6" y="11.5" width="7" height="3.5" fill="#17a9b8" stroke="#141b33" stroke-width="1.1"/>
        </svg>F:&nbsp;&nbsp;(850) 555-0181
      </li>
    </ul>

    <p class="address">487 Orchard Lane,<br>Suite 210, Tallahassee,<br>FL 32308</p>

    <p class="brand-vertical">Havenry</p>
  </section>

  <section class="deliverables">
    <p class="deliverables__heading">Deliverables for any chosen concept included:</p>
    <ul class="deliverables__list">
      <li>· Fully layered, editable PSD (organised text layers)</li>
      <li>· AI/EPS vector files for print precision</li>
      <li>· Print-ready PDF (CMYK, bleed, crop marks)</li>
      <li>· Fonts and assets packaged for easy use</li>
    </ul>
  </section>

</body>
</html>
```